Business Card for a Wedding Films Business

We require a business card design for our business 'Lewis Marrow Wedding Films'. The logo needs to look classy and high end.

Target Market(s)

Wedding Couples

Contact Information for Business Card

Lewis Marrow Wedding Films
07312 605 227
films@lewismarrowreels.com
www.lewismarrowreels.com

Facebook: @lewismarrowweddingfilms
Instagram: @lewismarrowfilms

Font styles to use
Sans Serif

Requirements
Must have
• Social media icons - Facebook and Instagram

```html
<!DOCTYPE html>
<html lang="en">
<head>
<meta charset="utf-8">
<title>Lewis Marrow Wedding Films – Business Card</title>
<link href="https://fonts.googleapis.com/css2?family=Open+Sans:wght@400;600&display=swap" rel="stylesheet">
<style>
  :root {
    --backdrop: #eef3ee;
    --card: #f1ece4;
    --ink: #1f1f1f;
    --ink-soft: #3a3a3a;
    --rose: #e7a2b8;
    --rose-pale: #f5dbe2;
    --lace: #f7f4ee;
    --gold: #d7a844;
  }
  * { box-sizing: border-box; margin: 0; padding: 0; }
  html, body { width: 1200px; height: 799px; overflow: hidden; }
  body {
    background: var(--backdrop);
    font-family: "Open Sans", Arial, sans-serif;
    color: var(--ink);
    position: relative;
  }
  .card {
    position: absolute;
    top: 185px;
    width: 290px;
    height: 440px;
    border-radius: 16px;
    background: var(--card);
    overflow: hidden;
    box-shadow: 0 3px 8px rgba(0,0,0,0.12);
  }
  .card--front { left: 290px; }
  .card--back { left: 620px; }

  .photo { position: absolute; }
  .photo--lace {
    top: 0; right: 0; width: 95px; height: 100%;
    background: linear-gradient(90deg, rgba(247,244,238,0) 0%, var(--lace) 40%, #ebe5da 100%);
  }
  .photo--roses-top {
    top: 0; left: 0; width: 100%; height: 150px;
    background:
      radial-gradient(ellipse 75px 65px at 60px 55px, var(--rose) 0%, var(--rose-pale) 55%, rgba(245,219,226,0) 100%),
      radial-gradient(circle 30px at 210px 95px, rgba(215,168,68,0.55) 0%, rgba(215,168,68,0) 100%);
  }
  .photo--roses-bottom {
    bottom: 0; left: 0; width: 100%; height: 150px;
    background:
      radial-gradient(ellipse 80px 65px at 115px 95px, var(--rose) 0%, var(--rose-pale) 55%, rgba(245,219,226,0) 100%),
      radial-gradient(ellipse 40px 55px at 10px 70px, var(--rose-pale) 0%, rgba(245,219,226,0) 100%),
      radial-gradient(circle 32px at 225px 30px, rgba(215,168,68,0.55) 0%, rgba(215,168,68,0) 100%);
  }

  .brand {
    position: absolute;
    width: 200px;
    text-align: center;
    color: var(--ink);
    font-weight: 600;
    text-transform: uppercase;
  }
  .card--front .brand { left: 65px; top: 172px; }
  .card--back .brand { left: 20px; top: 95px; }
  .brand__mark {
    display: block;
    width: 40px; height: 40px;
    margin: 0 auto 6px;
    border: 3px solid var(--ink);
  }
  .brand__name {
    display: block;
    font-size: 17px;
    letter-spacing: 3px;
    line-height: 1.2;
  }
  .brand__tag {
    display: block;
    font-size: 8px;
    letter-spacing: 3.5px;
    line-height: 1.4;
  }

  .contact {
    position: absolute;
    left: 97px; top: 308px;
    width: 175px;
    font-size: 12px;
    color: var(--ink-soft);
  }
  .contact__row {
    display: flex; align-items: center; gap: 7px;
    height: 18px; white-space: nowrap;
  }
  .contact__row--social { font-size: 10px; height: 16px; }
  .contact__icon { width: 10px; height: 10px; flex: none; }
  .contact__badge {
    width: 9px; height: 9px; flex: none;
    border: 1.5px solid var(--ink-soft); border-radius: 2px;
  }
  .contact__rule {
    height: 1.5px; background: var(--ink-soft);
    margin: 6px 0 8px;
    width: 158px;
  }
  .web {
    position: absolute;
    left: 55px; top: 262px;
    font-size: 11px;
    color: var(--ink);
  }
</style>
</head>
<body>

  <section class="card card--front">
    <div class="photo photo--roses-top" role="img" aria-label="Pink frosted rose and gold wedding rings"></div>
    <div class="photo photo--lace" role="img" aria-label="White embossed lace pattern"></div>

    <p class="brand">
      <span class="brand__mark"></span>
      <span class="brand__name">Lewis Marrow</span>
      <span class="brand__tag">Wedding Films</span>
    </p>

    <div class="contact">
      <div class="contact__row">
        <svg class="contact__icon" viewBox="0 0 10 10"><rect x="2.5" y="0.5" width="5" height="9" rx="1" fill="none" stroke="currentColor"/><circle cx="5" cy="8" r="0.6" fill="currentColor"/></svg>
        <span>07312 605 227</span>
      </div>
      <div class="contact__row">
        <svg class="contact__icon" viewBox="0 0 10 10"><rect x="0.5" y="2" width="9" height="6" fill="none" stroke="currentColor"/><path d="M0.5 2 L5 5.5 L9.5 2" fill="none" stroke="currentColor"/></svg>
        <span>films@lewismarrowreels.com</span>
      </div>
      <div class="contact__rule"></div>
      <div class="contact__row contact__row--social">
        <span class="contact__badge"></span>
        <span>@lewismarrowweddingfilms</span>
      </div>
      <div class="contact__row contact__row--social">
        <span class="contact__badge"></span>
        <span>@lewismarrowfilms</span>
      </div>
    </div>
  </section>

  <section class="card card--back">
    <div class="photo photo--lace" role="img" aria-label="White embossed lace pattern"></div>
    <div class="photo photo--roses-bottom" role="img" aria-label="Pink frosted roses and gold wedding rings"></div>

    <p class="brand">
      <span class="brand__mark"></span>
      <span class="brand__name">Lewis Marrow</span>
      <span class="brand__tag">Wedding Films</span>
    </p>
    <p class="web">www.lewismarrowreels.com</p>
  </section>

</body>
</html>
```